8.5" x 11" BookLet Hydroponic & Garden Supply

It's a Booklet catalog which advertising products.
We need a designer that stand out our company and our products in this catalog. Must keep all information in the PDF. Must keep all products pictures. Brand name banners keep as much as the designer can.
Please look at the attachment for the PDF booklet catalog and Lay Out Guideline from Printing company requirement.

Target Market(s)

Hydroponic and Garden green house

Industry/Entity Type

It Company

Font styles to use
Serif

Colors
ec1f27
0255a3
9bcb3b
6b449b
a64599
00a990

Requirements
Must have
• Must keep products and prices and products' pictures.

```html
<!DOCTYPE html>
<html lang="en">
<head>
<meta charset="utf-8">
<title>2 in 1 Automatic Trimmer</title>
<link rel="stylesheet" href="https://fonts.googleapis.com/css2?family=Audiowide&family=Michroma&family=Open+Sans:wght@400;700;800&family=Tinos:wght@400;700&display=swap">
<style>
  :root {
    --red: #ec1f27;
    --red-dark: #a3243a;
    --blue: #0255a3;
    --green: #9bcb3b;
    --teal: #00a990;
    --paper: #ffffff;
    --backdrop: #eceae6;
    --shadow-grey: #d5d5d5;
  }
  * { margin: 0; padding: 0; box-sizing: border-box; }
  html, body { width: 1200px; height: 1200px; overflow: hidden; background: var(--backdrop); }
  .page {
    position: absolute; left: 151px; top: 24px;
    width: 1020px; height: 1310px;
    background: var(--paper);
    transform: scale(0.88); transform-origin: top left;
    box-shadow: 0 6px 24px rgba(0,0,0,.18);
  }
  .title-band { position: absolute; left: 0; top: 57px; width: 1020px; height: 86px; }
  .title-band svg { position: absolute; inset: 0; }
  .title {
    position: absolute; left: 57px; top: 24px;
    font-family: "Audiowide", sans-serif; font-size: 31px; color: #fff; letter-spacing: .5px;
  }
  .item-no {
    position: absolute; right: 56px; top: 14px; text-align: center;
    font-family: "Michroma", sans-serif; font-size: 22px; line-height: 27px; color: #fff;
  }
  .photo { position: absolute; border-radius: 4px; }
  .photo-trimmer { left: 85px; top: 225px; width: 260px; height: 450px;
    background: linear-gradient(180deg, #d4d6d8 0%, #b9bcbf 45%, #2a2c2e 60%, #1d1e20 100%); }
  .photo-bucket { left: 360px; top: 183px; width: 150px; height: 200px; border-radius: 10px;
    background: linear-gradient(180deg, #141414 0%, #6c5a7a 45%, #8b8a4d 70%, #141414 100%); }
  .cert { position: absolute; top: 690px; background: #2b2b2b; }
  .cert-a { left: 216px; width: 52px; height: 40px; border-radius: 4px; }
  .cert-b { left: 288px; width: 80px; height: 40px; border-radius: 50%; }
  .price-banner { position: absolute; left: 0; top: 775px; width: 495px; height: 112px; }
  .price-banner svg { position: absolute; inset: 0; }
  .price-text { position: absolute; left: 58px; top: 12px; color: #fff; font-family: "Open Sans", sans-serif; }
  .price-label { font-size: 28px; font-weight: 700; letter-spacing: .5px; line-height: 32px; }
  .price-amount { font-size: 38px; font-weight: 800; line-height: 48px; }
  .price-amount .unit { font-size: 28px; font-weight: 700; }
  .price-amount .note { font-size: 28px; font-weight: 400; }
  .promo { position: absolute; left: 57px; top: 908px; font-family: "Open Sans", sans-serif; color: var(--blue); }
  .promo-head { font-size: 39px; font-weight: 800; letter-spacing: .3px; line-height: 52px; }
  .promo-sub { margin-top: 6px; font-size: 29px; line-height: 32px; }
  .details { position: absolute; left: 539px; top: 187px; width: 440px; font-family: "Tinos", serif; font-size: 21.5px; line-height: 25.3px; }
  .gift { color: var(--red); font-weight: 700; }
  .summary { color: var(--blue); margin-top: 25px; }
  .features { list-style: none; margin-top: 25px; color: var(--blue); }
  .features li { position: relative; padding-left: 28px; }
  .features li::before { content: ""; position: absolute; left: 2px; top: 6px; width: 13px; height: 13px; background: var(--teal); }
  .warranty { color: var(--teal); font-weight: 700; margin-top: 25px; }
  .msrp { color: var(--teal); font-weight: 700; margin-top: 24px; }
</style>
</head>
<body>
<main class="page">
  <header class="title-band">
    <svg width="1020" height="86" viewBox="0 0 1020 86">
      <rect width="1020" height="86" fill="var(--green)"/>
      <polygon points="805,0 1020,0 1020,86 765,86" fill="var(--blue)"/>
    </svg>
    <h1 class="title">2 in 1 Automatic Trimmer</h1>
    <div class="item-no">ITEM<br>#LCC01</div>
  </header>

  <div class="photo photo-trimmer" role="img" aria-label="Photo of the 2 in 1 automatic trimmer with mesh collection bag on a steel stand"></div>
  <div class="photo photo-bucket" role="img" aria-label="Photo of a black bucket of BudMass nutrient"></div>
  <div class="cert cert-a"></div>
  <div class="cert cert-b"></div>

  <div class="price-banner">
    <svg width="495" height="112" viewBox="0 0 495 112">
      <polygon points="0,4 495,4 462,56 495,108 0,108" fill="var(--shadow-grey)"/>
      <defs>
        <linearGradient id="bannerFill" x1="0" x2="1">
          <stop offset="0" stop-color="var(--red-dark)"/>
          <stop offset=".55" stop-color="var(--red)"/>
        </linearGradient>
      </defs>
      <polygon points="0,0 485,0 452,52 485,104 0,104" fill="url(#bannerFill)"/>
    </svg>
    <div class="price-text">
      <div class="price-label">WHOLESALE</div>
      <div class="price-amount">$750 <span class="unit">each</span> <span class="note">(Free Shipping)</span></div>
    </div>
  </div>

  <section class="promo">
    <div class="promo-head">BUY 10 GET 1 FREE</div>
    <div class="promo-sub">+ Free 10 qty 300g or<br>500g BudMass Products.</div>
  </section>

  <section class="details">
    <p class="gift">FREE 500g BudMass<br>BudMass for Bud Tight &amp; Bud Heavier<br>Retail Value $100.00 (500g)</p>
    <p class="summary">The automatic trimmer is contained system with the sturdy frame, supports a hermitically sealed cutter box with stainless steel cutter blades and screen surrounded by a safety shroud and base assembly. This system is specifically designed for use in the processing of cash crops including basil, coriander, lavender, mint, parsley oregano and rosemary. Below is a summary of some of the features of this outstanding automatic trimmer.</p>
    <ul class="features">
      <li>2 carry bags</li>
      <li>1 Plastic Ball (for circulate flowers to allow for better trimming)</li>
      <li>Mesh bag</li>
      <li>Stainless steel adjustable powerful triple blade &amp; Lazar cut fans</li>
      <li>4 removable grills (1 standard grate &amp; 1 finger grate for the bottom part square trimmer. 1 standard grate &amp; 1/4” grate for the top glass top part. ( easy clean or replaceable new grate)</li>
      <li>Strongest powerful high quality efficiency quiet motor</li>
      <li>2 in 1 trimmer capability to go to manual mode with top class part removal.</li>
      <li>Designed with auto shut off safety feature when cutting box is opened</li>
    </ul>
    <p class="warranty">One Year Warranty on Motor &amp;<br>Electric components</p>
    <p class="msrp">MSR$1,500 ea.</p>
  </section>
</main>
</body>
</html>
```